Ayurveda & Wellness Website Redesign.

I need my website www.quilarest.com re-skinned. It is a wordpress site with Divi Builder.
I need a clearer funnel for new clients on the home page.
The funnel should provide questions for the potential client to answer. I can provide these, but I need a better funnel mechanism I think,
Possibly a video on the home page. Or an area of a video that I can change out.
So a better landing page is KEY!
The funnel should reroute to a video page and I should get informed when new clients enroll in the funnel.
Maybe I need a management system for this, but I need a recommendation.
Now I am using forms manager.
I need to be able to make changes using wordpress and/or Divi Builder.
The website should have a clean and spiritual feeling.
I can provide many more pictures and higher resolution.
I like the feeling of this website: http://tarnhollowherbals.com
Also this website: http://calmpetalroots.com/sessionswithorvena/
Target Market(s)
Women ages 25-65. People interested in health, yoga, spirituality.
Industry/Entity Type
Health And Wellness
Coding
Coded - Design and coding required
Requirements
Must have
- A clear sales funnel/enrollment mechanism on the home page. Could have a ebook download (I will provide) when they enroll.
Nice to have
- Currently using Slotra for clients to enroll in appointments. I would like to keep this.

```html
<!DOCTYPE html>
<html lang="en">
<head>
<meta charset="utf-8">
<title>Quila Rest — Ayurvedic &amp; Wellness Provider</title>
<link rel="stylesheet" href="https://fonts.googleapis.com/css2?family=Open+Sans:wght@400;600;700&family=Montserrat:wght@600;700&display=swap">
<style>
:root{
  --orange:#f39a1e;
  --orange-dark:#d9831a;
  --ink:#333333;
  --muted:#666666;
  --light:#f2f2f2;
  --white:#ffffff;
  --line:#cfcfcf;
}
*{box-sizing:border-box;margin:0;padding:0}
html,body{width:1200px;height:4400px;overflow:hidden}
body{position:relative;font-family:"Open Sans",Arial,sans-serif;color:var(--ink);background:var(--white)}
.abs{position:absolute}
.section{position:absolute;left:0;width:1200px}

/* Hero */
.hero{top:0;height:637px;background:linear-gradient(135deg,#2f6fa8 0%,#3f86c4 30%,#6d4f86 45%,#3a2a22 70%,#7a3a22 100%)}
.brand{font-family:"Open Sans",Arial,sans-serif;font-weight:400;font-size:40px;letter-spacing:1px;color:var(--white)}
.hero .brand{left:131px;top:28px}
.nav{left:460px;top:51px;display:flex;gap:0;font-size:13px;color:var(--white)}
.nav a{color:var(--white);text-decoration:none;padding:4px 0}
.nav .item{position:absolute;top:0;white-space:nowrap}
.nav .active{background:var(--orange);padding:6px 12px;top:-5px}
.phone-tab{left:900px;top:0;width:170px;height:31px;background:var(--white);border-radius:0 0 4px 4px;display:flex;align-items:center;justify-content:center;gap:6px;font-size:10px;color:var(--ink)}
.phone-tab strong{font-size:13px;font-weight:700}
.play{left:554px;top:246px}
.hero-title{left:0;width:1200px;top:432px;text-align:center;color:var(--white)}
.hero-title .big{font-family:"Montserrat",Arial,sans-serif;font-weight:700;font-size:42px;line-height:54px;display:block}
.hero-title .small{font-size:38px;font-weight:400;line-height:46px;display:block}
.dots{display:flex;gap:24px}
.hero .dots{left:534px;top:574px}
.dot{width:9px;height:9px;border-radius:50%;background:var(--white)}
.dot.ring{background:transparent;border:2px solid var(--white)}

/* Signup */
.signup{top:637px;height:406px;background:var(--light)}
.signup h2{position:absolute;top:80px;left:0;width:1200px;text-align:center;color:var(--orange);font-weight:600;font-size:26px;line-height:36px;letter-spacing:.5px}
.field{position:absolute;height:45px;background:var(--white);border:1px solid var(--line);font-size:12px;color:var(--muted);padding:0 16px;display:flex;align-items:center}
.btn{position:absolute;background:var(--orange);color:var(--white);font-weight:700;font-size:15px;letter-spacing:1px;display:flex;align-items:center;justify-content:center}

/* Services */
.services{top:1043px;height:780px;background:var(--white)}
.photo{position:absolute}
.heading{position:absolute;color:var(--orange);font-weight:600;font-size:26px;letter-spacing:.3px}
.underline{position:absolute;width:54px;height:2px;background:var(--orange)}
.service{position:absolute;width:200px;text-align:center;font-size:15px;color:var(--ink)}
.service svg{display:block;margin:0 auto 16px}
.book-box{left:686px;top:449px;width:383px;height:147px;background:var(--orange);color:var(--white);text-align:center}
.book-box h3{margin-top:18px;font-family:"Montserrat",Arial,sans-serif;font-weight:700;font-size:23px;line-height:28px}
.book-box p{font-size:23px;line-height:28px}
.book-box .cta{position:absolute;left:111px;top:93px;width:162px;height:36px;background:var(--orange-dark);font-size:11px;font-weight:700;display:flex;align-items:center;justify-content:center;letter-spacing:.5px}

/* Banner */
.banner{top:1823px;height:603px;background:linear-gradient(180deg,#5b3a28 0%,#6b4330 50%,#4e3020 100%)}
.banner h2{position:absolute;top:165px;left:0;width:1200px;text-align:center;color:var(--white);font-family:"Montserrat",Arial,sans-serif;font-weight:700;font-size:31px;line-height:42px;letter-spacing:.5px}
.banner p{position:absolute;top:282px;left:0;width:1200px;text-align:center;color:var(--white);font-size:18px;line-height:28px}
.outline-btn{position:absolute;left:515px;top:384px;width:170px;height:46px;border:2px solid var(--white);color:var(--white);font-family:"Montserrat",Arial,sans-serif;font-weight:700;font-size:17px;display:flex;align-items:center;justify-content:center;gap:8px}

/* About */
.about{top:2426px;height:498px;background:var(--white)}
.about .lead{position:absolute;left:673px;top:180px;width:400px;font-size:13px;line-height:24px;font-weight:600}
.about .body{position:absolute;left:673px;top:240px;width:400px;font-size:12.5px;line-height:24px;color:var(--muted)}
.small-btn{position:absolute;left:674px;top:404px;width:110px;height:39px;border:1px solid var(--orange);color:var(--orange);font-size:12px;font-weight:600;display:flex;align-items:center;justify-content:center}

/* Offerings */
.offerings{top:2924px;height:545px;background:var(--light)}
.offer{position:absolute;width:260px;text-align:center;font-size:15px}
.offer svg{display:block;margin:0 auto 14px}

/* Testimonials */
.testimonials{top:3469px;height:522px;background:var(--white)}
.testimonials .heading{left:0;width:1200px;text-align:center;top:70px}
.card{position:absolute;top:193px;width:323px;height:191px;background:var(--orange);color:var(--white);padding:28px 33px;font-size:11px;line-height:20px}
.card .q{text-align:justify;opacity:.95}
.card .by{position:absolute;left:33px;top:152px;font-weight:700;font-size:11px}
.card .arrow{position:absolute;top:84px;width:0;height:0;border-top:12px solid transparent;border-bottom:12px solid transparent}
.card.left .arrow{left:-12px;border-right:12px solid var(--orange)}
.card.right .arrow{right:-12px;border-left:12px solid var(--orange)}
.avatar{position:absolute;width:82px;height:82px;border-radius:50%;background:linear-gradient(160deg,#bdbdbd,#6f6f6f)}
.testimonials .dots{left:573px;top:434px;gap:11px}
.testimonials .dot{width:7px;height:7px;background:#c8c8c8}
.testimonials .dot.on{background:var(--ink)}

/* Footer */
.footer{top:3991px;height:409px;background:var(--light)}
.footer .brand{left:131px;top:66px;color:var(--ink);font-size:38px}
.footer h4{position:absolute;font-size:11px;font-weight:700;letter-spacing:.5px}
.social{position:absolute;top:204px;width:32px;height:32px;border-radius:50%;background:var(--orange)}
.menu-list{position:absolute;left:512px;top:99px;list-style:none;font-size:10.5px;line-height:20.5px}
.footer .field{height:43px;font-size:11px}
.copyright{position:absolute;top:4353px;left:0;width:1200px;text-align:center;font-size:10px;color:var(--ink)}
</style>
</head>
<body>

<header class="section hero" role="img" aria-label="Photo of purple bath salts in a wooden bowl with white orchids on a blue wooden table">
  <div class="abs brand">Quila Rest</div>
  <nav class="abs nav" style="width:620px;height:30px">
    <a class="item active" style="left:0">Home</a>
    <a class="item" style="left:76px">Consults</a>
    <a class="item" style="left:159px">Ayurveda</a>
    <a class="item" style="left:248px">About</a>
    <a class="item" style="left:318px">Workshops</a>
    <a class="item" style="left:409px">Testimonials</a>
    <a class="item" style="left:515px">Blog</a>
    <a class="item" style="left:565px">Contact</a>
  </nav>
  <div class="abs phone-tab">
    <svg width="12" height="12" viewBox="0 0 24 24"><path d="M6.6 10.8a15 15 0 0 0 6.6 6.6l2.2-2.2a1 1 0 0 1 1-.25 11.4 11.4 0 0 0 3.6.6 1 1 0 0 1 1 1V20a1 1 0 0 1-1 1A17 17 0 0 1 3 4a1 1 0 0 1 1-1h3.5a1 1 0 0 1 1 1c0 1.25.2 2.45.6 3.6a1 1 0 0 1-.25 1z" fill="#333"/></svg>
    <span>CALL :</span><strong>555-204-7316</strong>
  </div>
  <svg class="abs play" width="92" height="92" viewBox="0 0 92 92">
    <circle cx="46" cy="46" r="42" fill="rgba(255,255,255,0.15)" stroke="#ffffff" stroke-width="5"/>
    <path d="M37 28 L66 46 L37 64 Z" fill="#ffffff"/>
  </svg>
  <h1 class="abs hero-title"><span class="big">AYURVEDIC &amp;</span><span class="small">Wellness provider</span></h1>
  <div class="abs dots"><span class="dot"></span><span class="dot ring"></span><span class="dot"></span><span class="dot"></span><span class="dot"></span></div>
</header>

<section class="section signup">
  <h2>SIGN UP HERE FOR A FREE AYURVEDIC WELLNESS<br>ASSESSMENT WITH MAREN SOLANO, PHD</h2>
  <div class="field" style="left:261px;top:194px;width:208px">Name</div>
  <div class="field" style="left:495px;top:194px;width:208px">Email Address</div>
  <div class="field" style="left:729px;top:194px;width:208px">Phone No</div>
  <div class="btn" style="left:543px;top:285px;width:112px;height:46px">SUBMIT</div>
</section>

<section class="section services">
  <div class="photo" style="left:40px;top:67px;width:404px;height:648px;background:radial-gradient(ellipse at 45% 50%,#3a3a3a 0%,#6b6b6b 30%,#ffffff 62%)" role="img" aria-label="Photo of a woman in black yoga clothes kneeling in meditation"></div>
  <h2 class="heading" style="left:427px;top:98px">OUR SERVICES</h2>
  <div class="underline" style="left:427px;top:152px"></div>

  <div class="service" style="left:361px;top:218px">
    <svg width="70" height="70" viewBox="0 0 70 70" fill="none" stroke="#f39a1e" stroke-width="4" stroke-linecap="round">
      <path d="M22 6c-3 4 3 6 0 10M32 6c-3 4 3 6 0 10M42 6c-3 4 3 6 0 10"/>
      <path d="M8 26h54c0 16-12 26-27 26S8 42 8 26z"/>
      <circle cx="46" cy="46" r="10"/>
    </svg>Ayurvedic
  </div>
  <div class="service" style="left:641px;top:218px">
    <svg width="70" height="70" viewBox="0 0 70 70" fill="none" stroke="#f39a1e" stroke-width="4" stroke-linejoin="round">
      <path d="M35 8c8 10 8 26 0 36-8-10-8-26 0-36z"/>
      <path d="M35 44c-10-2-20-10-22-24 10 2 18 8 22 24zM35 44c10-2 20-10 22-24-10 2-18 8-22 24z"/>
      <path d="M35 44c-8 6-18 8-28 6M35 44c8 6 18 8 28 6M35 44v16"/>
    </svg>Ayurvedic Herbs
  </div>
  <div class="service" style="left:863px;top:218px">
    <svg width="70" height="70" viewBox="0 0 70 70" fill="none" stroke="#f39a1e" stroke-width="4" stroke-linecap="round">
      <circle cx="35" cy="35" r="14"/><circle cx="35" cy="35" r="6"/>
      <path d="M35 5v8M35 57v8M5 35h8M57 35h8M14 14l6 6M50 50l6 6M56 14l-6 6M20 50l-6 6"/>
    </svg>Community
  </div>
  <div class="service" style="left:361px;top:453px">
    <svg width="70" height="70" viewBox="0 0 70 70" fill="none" stroke="#f39a1e" stroke-width="4" stroke-linecap="round">
      <path d="M10 22c6-8 20-6 18 4-1 6-8 7-12 7 8 0 14 4 12 12-2 9-14 10-20 2"/>
      <path d="M30 36c4-6 12-6 14 2 2 8-2 16-6 20M44 38c4-4 14-4 14 6s-6 16-14 16"/>
      <path d="M40 10c4 4 10 4 14 0"/><circle cx="52" cy="22" r="2.5" fill="#f39a1e"/>
    </svg>Spritualality
  </div>

  <div class="abs book-box">
    <h3>BOOK YOUR FREE</h3>
    <p>information call</p>
    <div class="cta">CLICK HERE</div>
  </div>
</section>

<section class="section banner" role="img" aria-label="Photo of bowls of colourful spices and herbs on a dark wooden table">
  <h2>PERSONAL GUIDANCE FOR BRINGING MIND,<br>BODY AND SPIRIT INTO BALANCE</h2>
  <p>The magic of this program is that we have the space of an entire year<br>to create lasting habits and deep wellness.</p>
  <div class="outline-btn">READ MORE
    <svg width="8" height="10" viewBox="0 0 8 10"><path d="M1 0l6 5-6 5z" fill="#ffffff"/></svg>
  </div>
</section>

<section class="section about">
  <div class="photo" style="left:131px;top:100px;width:473px;height:342px;background:linear-gradient(180deg,#e9ecee 0%,#dfe4e7 45%,#7f8f99 62%,#8a7a62 80%,#6e5e45 100%)" role="img" aria-label="Photo of a woman in a turquoise top meditating on a rocky seashore"></div>
  <h2 class="heading" style="left:669px;top:88px">ABOUT MAREN</h2>
  <div class="underline" style="left:669px;top:135px;width:84px"></div>
  <p class="lead">I am passionate about energy renewal and helping people re-solve their health imbalances.</p>
  <p class="body">I have been studying and learning about Ayurveda for many years and have studied Clinical Ayurveda, Ayurvedic Spiritual Counseling and Jyotish (Vedic Astrology) under Dr. Elias Marrow of Riverstone Ayurveda. I have also studied Jyotish with Delia Varga.&nbsp; I offer private consults and workshops on Ayurveda and wellness.</p>
  <div class="small-btn">READ MORE</div>
</section>

<section class="section offerings">
  <h2 class="heading" style="left:131px;top:60px">OUR OFFERINGS</h2>
  <div class="underline" style="left:131px;top:109px"></div>

  <div class="offer" style="left:89px;top:176px">
    <svg width="62" height="62" viewBox="0 0 70 70" fill="none" stroke="#f39a1e" stroke-width="4" stroke-linejoin="round">
      <path d="M35 10c8 10 8 24 0 34-8-10-8-24 0-34z"/>
      <path d="M35 44c-10-2-20-10-22-24 10 2 18 8 22 24zM35 44c10-2 20-10 22-24-10 2-18 8-22 24z"/>
      <path d="M18 56h34"/>
    </svg>Heart Based Meditation
  </div>
  <div class="offer" style="left:404px;top:176px">
    <svg width="62" height="62" viewBox="0 0 70 70" fill="none" stroke="#f39a1e" stroke-width="3.5" stroke-linejoin="round">
      <path d="M35 8L58 48H12Z"/><path d="M35 62L12 22H58Z"/><circle cx="35" cy="35" r="8"/>
    </svg>Chakra Balancing
  </div>
  <div class="offer" style="left:89px;top:362px">
    <svg width="62" height="62" viewBox="0 0 70 70" fill="none" stroke="#f39a1e" stroke-width="4" stroke-linecap="round">
      <path d="M8 32h54c0 14-12 24-27 24S8 46 8 32z" fill="#f39a1e"/>
      <path d="M40 30L58 8"/><path d="M24 62h22"/>
    </svg>Ayurvedic Nutrition
  </div>
  <div class="offer" style="left:404px;top:362px">
    <svg width="62" height="62" viewBox="0 0 70 70" fill="none" stroke="#f39a1e" stroke-width="4" stroke-linejoin="round">
      <path d="M30 4l8 8-8 8-8-8z"/>
      <path d="M14 30h36v14c0 10-8 18-18 18S14 54 14 44z"/>
      <path d="M50 36c8 0 10 10 0 12"/>
    </svg>Ayurvedic Teas and Spices
  </div>

  <div class="photo" style="left:708px;top:46px;width:492px;height:499px;background:linear-gradient(180deg,#f2f2f2 0%,#ececec 40%,#a99478 75%,#7a6550 100%)" role="img" aria-label="Photo of a woman in a turquoise top sitting cross-legged with hands in prayer pose outdoors"></div>
</section>

<section class="section testimonials">
  <h2 class="heading">TESTIMONIALS</h2>
  <div class="underline" style="left:569px;top:125px;width:62px"></div>

  <div class="avatar" style="left:162px;top:245px" role="img" aria-label="Client portrait"></div>
  <div class="card left" style="left:270px">
    <span class="arrow"></span>
    <p class="q">After Maren Solano' attentive questions, feeling of my pulses, and intuitive observation, she prescribed for me a blend of herbs and suggestions for my diet that allow me to sleep through the night without my...</p>
    <span class="by">M.S.</span>
  </div>
  <div class="card right" style="left:609px">
    <span class="arrow"></span>
    <p class="q" style="text-align:left">My experience with Maren as my Ayurvedic practitioner far exceeded any expectation I may have had. She is exceptionally knowledgeable, and has a natural gift of sharing information in a way that is easy to understand...</p>
    <span class="by">D.D.</span>
  </div>
  <div class="avatar" style="left:958px;top:245px" role="img" aria-label="Client portrait"></div>

  <div class="abs dots"><span class="dot"></span><span class="dot on"></span><span class="dot"></span><span class="dot"></span></div>
</section>

<footer class="section footer">
  <div class="abs brand">Quila Rest</div>
  <h4 style="left:226px;top:160px">FOLLOW US</h4>
  <span class="social" style="left:196px" aria-label="Social link"></span>
  <span class="social" style="left:243px" aria-label="Social link"></span>
  <span class="social" style="left:291px" aria-label="Social link"></span>

  <h4 style="left:512px;top:66px">MENU</h4>
  <ul class="menu-list">
    <li>Home</li><li>Consults</li><li>Ayurveda</li><li>About</li><li>Workshops</li><li>Testimonials</li><li>Blog</li>
  </ul>

  <h4 style="left:691px;top:66px">NEWSLETTER SIGNUP!</h4>
  <div class="field" style="left:693px;top:106px;width:180px">Name</div>
  <div class="field" style="left:889px;top:106px;width:180px">E mail</div>
  <div class="btn" style="left:968px;top:184px;width:101px;height:33px;font-size:11px">SUBSCRIBE</div>
</footer>
<p class="copyright">Copyrights @ 2017 All Rights Reserved</p>

</body>
</html>
```